Business Card Design - Kestrel Tidewave

We (Kestrel Tidewave) need a business card design for our boutique mobile marketing agency based in Sydney, Australia.
We work with brands and advertisers to deliver and implement end to end mobile (smartphone and tablet) marketing solutions.

We already have a logo and website design, these files will be provided. Our colours centre around a blue/orange mix (the logo containing the orange (colour code: RGB 255,165,0).

Our name and logo communicate strength and confidence. We see ourselves as being trustworthy advisors who are also fun and passionate.

Target Market(s)

Senior Marketing Managers

Industry/Entity Type

Marketing

Requirements
Must have
• Employee Name: Tamsin Vareley
Mobile Number: 0491 570 156
Email Address xxxx@kestreltidewave.example
Website: www.kestreltidewave.example
Twitter ID: KestrelTidewave

```html
<!DOCTYPE html>
<html lang="en">
<head>
<meta charset="utf-8">
<title>Kestrel Tidewave – Business Card</title>
<link rel="stylesheet" href="https://fonts.googleapis.com/css2?family=Open+Sans:wght@400;600;700&display=swap">
<style>
  :root {
    --accent: #ee4324;
    --charcoal: #363636;
    --charcoal-faint: #3e3e3e;
    --paper: #ffffff;
    --canvas: #f4f4f4;
    --ink: #4a4a4a;
    --muted: #9a9a9a;
  }
  * { margin: 0; padding: 0; box-sizing: border-box; }
  html, body {
    width: 1200px; height: 900px; overflow: hidden;
    background: var(--canvas);
    font-family: "Open Sans", Arial, sans-serif;
  }
  .stage { position: relative; width: 1200px; height: 900px; }

  .card {
    position: absolute; top: 300px;
    width: 505px; height: 290px;
    overflow: hidden;
  }
  .card--front { left: 75px; background: var(--paper); }
  .card--back { left: 620px; background: var(--charcoal); }

  .wordmark {
    position: absolute;
    font-weight: 600;
    letter-spacing: 0.5px;
    white-space: nowrap;
    line-height: 1;
  }
  .card--front .wordmark { top: 34px; right: 28px; font-size: 22px; color: var(--accent); }
  .card--back .wordmark { top: 132px; right: 30px; font-size: 34px; color: var(--paper); }

  .emblem-area {
    position: absolute; border-radius: 50%;
  }
  .card--front .emblem-area {
    left: -30px; bottom: -70px; width: 200px; height: 200px;
    background: var(--accent);
  }
  .card--back .emblem-area {
    left: 30px; bottom: -40px; width: 170px; height: 170px;
    background: var(--charcoal-faint);
  }

  .holder { position: absolute; left: 250px; top: 100px; }
  .holder__name {
    font-size: 22px; font-weight: 700; color: var(--accent);
    letter-spacing: -0.3px; line-height: 1;
  }
  .holder__title { font-size: 11px; color: var(--muted); margin-top: 4px; }

  .contact-list { list-style: none; margin-top: 12px; }
  .contact-list li {
    display: flex; align-items: center; gap: 7px;
    font-size: 13.5px; color: var(--ink); height: 20px;
    white-space: nowrap;
  }
  .contact-list svg { width: 13px; height: 13px; flex: none; }

  .rule-bottom {
    position: absolute; left: 165px; right: 0; bottom: 26px;
    height: 5px; background: var(--accent);
  }
  .rule-top {
    position: absolute; left: 0; right: 0; top: 0;
    height: 7px; background: var(--accent);
  }

  .signoff {
    position: absolute; right: 32px; bottom: 50px;
    font-size: 30px; font-weight: 600; color: var(--charcoal);
    letter-spacing: 0.5px; white-space: nowrap;
  }
</style>
</head>
<body>
<main class="stage">

  <section class="card card--front" aria-label="Business card front">
    <div class="wordmark">Kestrel Tidewave</div>
    <div class="emblem-area" role="img" aria-label="Brand emblem decoration"></div>

    <div class="holder">
      <div class="holder__name">TAMSIN VARELEY</div>
      <div class="holder__title">Job Title</div>
      <ul class="contact-list">
        <li>
          <svg viewBox="0 0 14 14" aria-hidden="true"><rect x="0.5" y="0.5" width="13" height="13" rx="2.5" fill="none" stroke="#4a4a4a"/><rect x="4.5" y="3" width="5" height="8" rx="1" fill="#4a4a4a"/></svg>
          0491 570 156
        </li>
        <li>
          <svg viewBox="0 0 14 14" aria-hidden="true"><rect x="0.5" y="0.5" width="13" height="13" rx="2.5" fill="none" stroke="#4a4a4a"/><rect x="3" y="4.5" width="8" height="5" fill="none" stroke="#4a4a4a"/><path d="M3 4.5 L7 7.5 L11 4.5" fill="none" stroke="#4a4a4a"/></svg>
          xxxx@kestreltidewave.example
        </li>
        <li>
          <svg viewBox="0 0 14 14" aria-hidden="true"><rect x="0.5" y="0.5" width="13" height="13" rx="2.5" fill="none" stroke="#4a4a4a"/><circle cx="7" cy="7" r="3.5" fill="none" stroke="#4a4a4a"/><path d="M3.5 7 H10.5 M7 3.5 V10.5" stroke="#4a4a4a"/></svg>
          www.kestreltidewave.example
        </li>
        <li>
          <svg viewBox="0 0 14 14" aria-hidden="true"><rect x="0.5" y="0.5" width="13" height="13" rx="2.5" fill="none" stroke="#4a4a4a"/><rect x="4" y="4" width="6" height="6" fill="#4a4a4a"/></svg>
          KestrelTidewave
        </li>
      </ul>
    </div>
    <div class="rule-bottom"></div>
  </section>

  <section class="card card--back" aria-label="Business card back">
    <div class="rule-top"></div>
    <div class="emblem-area" role="img" aria-label="Faint brand emblem decoration"></div>
    <div class="wordmark">Kestrel Tidewave</div>
  </section>

  <div class="signoff">Kestrel Tidewave</div>
</main>
</body>
</html>
```